Eleven Daughters HAUNTED Through Youth (One clan sinking beneath old wrongs)

I want my book cover to coincide with the title. The "T" In Birth I want to be a cross with God on it. I want some of the letters melting. I also want a pit or a pool of fire with 9 fiery sisters drowning in it. It doesn't necessarily have to show the complete body, it can partial, some full, and some with just the hands coming out the fire like they have already drowned. The color of the cover I rather have it black since the fire is reddish, yellow/orange; but I'm open to creativity. My book should look like the place "Hell" since that's what my non-fiction book is all about. It's a true story of a struggling family living the hard knock life in New York with a vulnerable mother without our father in our lives. We experienced living in and out of shelter, getting picked on everywhere we went, school dropouts, young teen pregnancies, victims of rape, abuse, drug use, had a lot of witchcraft interventions as well as some of us giving our lives to the devil. As we gotten old we became more evil, indulged in the 7 deadly sins was their daily routine which caused tragedies to the family and others, our family values is no longer valued, and we grew apart as a whole. So my book is delivering a message to all families who has similar stories. Inspirational to whoever is seeking guidance and understanding as well as a wake up call to struggling family, evildoers, and people who are trying to transition.. Also, I want to bring families back together; most definitely mine because we all have some sort of Envy, Greed, Lust, Rage, Sloth, Gluttony, Self-Pride, etc. Giving this brief description of my book, the cover should reveal strictly evil. No smiles, just sinful. On the back of my cover I will have a short description of my book, and telling a little about myself, so I can have a little fire on it to blend in with the front, but it's optional. I'm also open to creative ideas, so if you can make a cover through your experience that goes with my title, I am willing to see them. My book is already done and is waiting to be published so the cover is the only thing I am waiting on. I hope this information is helpful, and I'm hoping I can get a book cover I am looking for.

• I'm undecided

• more than one person on the cover
• 9 fiery sisters drowning in a pool or pit of fire
• one person on the cover

```html
<!DOCTYPE html>
<html lang="en">
<head>
<meta charset="utf-8">
<title>Eleven Daughters HAUNTED Through Youth</title>
<link rel="stylesheet" href="https://fonts.googleapis.com/css2?family=Carlito:wght@700&display=swap">
<style>
  :root {
    --sky-top: #26303a;
    --sky-mid: #1b242d;
    --sky-low: #0e151d;
    --horizon: #0c1118;
    --lava-dark: #2a0c06;
    --fire-deep: #6e1806;
    --fire-red: #c7330c;
    --fire-orange: #ee7418;
    --fire-gold: #ffc24a;
    --fire-white: #fff1b8;
    --title-white: #ffffff;
    --tagline-orange: #f2a43c;
    --cross-wood: #4e321d;
    --cross-figure: #c69a6c;
  }
  * { box-sizing: border-box; margin: 0; padding: 0; }
  html, body { width: 800px; height: 1200px; overflow: hidden; background: #000; }
  .cover {
    position: relative; width: 800px; height: 1200px; overflow: hidden;
    font-family: "Carlito", "Calibri", Arial, sans-serif; font-weight: 700;
  }
  .storm-sky {
    position: absolute; left: 0; right: 0; top: 0; height: 720px;
    background:
      radial-gradient(ellipse 260px 120px at 150px 300px, rgba(130,135,125,0.35), transparent 70%),
      radial-gradient(ellipse 300px 140px at 260px 420px, rgba(80,90,95,0.35), transparent 70%),
      radial-gradient(ellipse 260px 120px at 620px 240px, rgba(95,105,110,0.3), transparent 70%),
      linear-gradient(180deg, var(--sky-top) 0%, var(--sky-mid) 45%, var(--sky-low) 100%);
  }
  .dark-hills {
    position: absolute; left: 0; right: 0; top: 600px; height: 130px;
    background: linear-gradient(180deg, #131b25 0%, var(--horizon) 100%);
  }
  .fire-pit {
    position: absolute; left: 0; right: 0; top: 640px; bottom: 0;
    background:
      radial-gradient(ellipse 70px 90px at 590px 70px, rgba(238,116,24,0.9), transparent 70%),
      radial-gradient(ellipse 60px 60px at 300px 20px, rgba(199,51,12,0.8), transparent 70%),
      radial-gradient(ellipse 240px 200px at 140px 180px, rgba(255,194,74,0.95), transparent 70%),
      radial-gradient(ellipse 180px 150px at 700px 160px, rgba(255,170,60,0.85), transparent 70%),
      radial-gradient(ellipse 300px 120px at 420px 330px, rgba(255,241,184,0.7), transparent 70%),
      radial-gradient(ellipse 220px 160px at 560px 260px, rgba(255,194,74,0.9), transparent 70%),
      radial-gradient(ellipse 260px 200px at 250px 380px, rgba(238,116,24,0.95), transparent 70%),
      radial-gradient(ellipse 500px 50px at 400px 110px, rgba(110,24,6,0.9), transparent 75%),
      radial-gradient(ellipse 200px 120px at 60px 520px, rgba(20,6,3,0.95), transparent 70%),
      radial-gradient(ellipse 260px 110px at 720px 540px, rgba(20,6,3,0.9), transparent 70%),
      linear-gradient(180deg, rgba(12,17,24,0) 0%, var(--lava-dark) 12%, var(--fire-deep) 20%, var(--fire-red) 38%, var(--fire-orange) 60%, var(--fire-red) 82%, var(--lava-dark) 100%);
  }
  .title {
    position: absolute; top: 22px; left: 0; width: 800px;
    text-align: center; color: var(--title-white); font-weight: 700;
    line-height: 0.95; letter-spacing: -1px;
  }
  .title-line { display: block; white-space: nowrap; }
  .title-line--first { font-size: 104px; }
  .title-line--shout { font-size: 168px; line-height: 0.86; }
  .title-line--last { font-size: 116px; }
  .crucifix {
    display: inline-block; width: 58px; height: 190px;
    vertical-align: -70px; margin: 0 4px;
    background: linear-gradient(180deg, var(--cross-wood) 0%, var(--cross-figure) 40%, var(--cross-wood) 100%);
    border-radius: 3px;
  }
  .melt-drips { position: absolute; top: 0; left: 0; width: 800px; height: 560px; pointer-events: none; }
  .tagline {
    position: absolute; top: 452px; left: 0; width: 820px;
    text-align: center; color: var(--tagline-orange);
    font-size: 31px; font-weight: 700; line-height: 1.22;
  }
</style>
</head>
<body>
  <main class="cover">
    <div class="storm-sky" role="img" aria-label="Dark stormy sky with heavy clouds and falling ash"></div>
    <div class="dark-hills" role="img" aria-label="Dim hills along the horizon"></div>
    <div class="fire-pit" role="img" aria-label="A pit of fire and lava with sisters sinking in the flames, some with only hands above the fire"></div>

    <h1 class="title">
      <span class="title-line title-line--first">Eleven Daughters</span>
      <span class="title-line title-line--shout">HAUNTED</span>
      <span class="title-line title-line--last">Through You<span class="crucifix" role="img" aria-label="Crucifix standing in for the letter t"></span>h</span>
    </h1>

    <svg class="melt-drips" viewBox="0 0 800 560" aria-hidden="true">
      <defs>
        <path id="drip" d="M-6 0 C-3 8 -1.8 25 -1.8 72 C-4.5 78 -5 84 -5 89 A5 5 0 0 0 5 89 C5 84 4.5 78 1.8 72 C1.8 25 3 8 6 0 Z"/>
      </defs>
      <g fill="#ffffff">
        <use href="#drip" transform="translate(218 96) scale(1 0.7)"/>
        <use href="#drip" transform="translate(330 98) scale(1 1.05)"/>
        <use href="#drip" transform="translate(452 98) scale(1 0.6)"/>
        <use href="#drip" transform="translate(520 96) scale(0.8 0.45)"/>
        <use href="#drip" transform="translate(586 96) scale(1 1.2)"/>
        <use href="#drip" transform="translate(140 244) scale(1 0.8)"/>
        <use href="#drip" transform="translate(300 244) scale(1 0.55)"/>
        <use href="#drip" transform="translate(420 244) scale(0.9 0.9)"/>
        <use href="#drip" transform="translate(508 244) scale(0.8 0.5)"/>
        <use href="#drip" transform="translate(612 244) scale(1 0.75)"/>
        <use href="#drip" transform="translate(112 360) scale(0.9 1.05)"/>
        <use href="#drip" transform="translate(160 360) scale(1.1 0.8)"/>
        <use href="#drip" transform="translate(205 360) scale(0.9 0.9)"/>
        <use href="#drip" transform="translate(290 364) scale(1 0.5)"/>
        <use href="#drip" transform="translate(372 364) scale(1.1 0.8)"/>
        <use href="#drip" transform="translate(470 364) scale(0.9 0.95)"/>
        <use href="#drip" transform="translate(615 370) scale(0.9 0.95)"/>
        <use href="#drip" transform="translate(680 364) scale(0.9 1.75)"/>
      </g>
    </svg>

    <p class="tagline">One clan sinking<br>beneath old wrongs</p>
  </main>
</body>
</html>
```